Four banner campaigns, much work to come!

I want banners created for 4 campaigns.

For each campaign I need these 6 banner sizes created:

? Web Banner Sizes (300x250, 728x90, 160x600)
One of each of these sizes, so 3 web banners

? Mobile Banner Sizes (300x50, 216x36, 240x240)

Campaign 1
http://www.cornerfirmratings.example/KLV-40275.html

Campaign 2
http://www.cornerfirmratings.example/Rockville-MD/Velunor-38412.html

Campaign 3
http://www.townlistingpages.example/m/orlando-fl-vacation-rentals/

Campaign 4
www.cornerfirmratings.example/The-Wexbridge-Institute-of-Sound-and-Screen-Studies-40269.html

I will send you numbers to edit each banner, so the 24 banners
will have 4 variations with different numbers. Same banners just
need you to send a copy with different phone numbers.

I want the work done today and I will post my next gig for the same winner.
Updates

I just want to make sure everyone knows this project is for 4 different banner campaigns.

Given banners in each size for each campaign.  I can submit additional info links if
needed let me know.  Please post more samples as soon as possible so I can pick
a designer to finish.

Thank you!

Industry/Entity Type

Radio

Requirements
Must have
• Messaging that follows the messaging in the pages I have submitted.
Nice to have
• Animated gif banners in general, QMV compliant.

```html
<!DOCTYPE html>
<html lang="en">
<head>
<meta charset="utf-8">
<title>Neighborhood Safety Banner Set</title>
<link rel="stylesheet" href="https://fonts.googleapis.com/css2?family=PT+Sans:ital,wght@0,400;0,700;1,700&family=PT+Sans+Narrow:wght@700&display=swap">
<style>
  :root {
    --board-top: #c4c4c4;
    --board-bottom: #f1f1f1;
    --blue-deep: #173c8c;
    --blue-mid: #2656b4;
    --blue-light: #3a78d4;
    --headline: #f6e54a;
    --copy: #ffffff;
    --button-top: #fff27a;
    --button-bottom: #f2b705;
    --button-edge: #c99200;
    --button-text: #1a1a1a;
    --photo-a: #e9d6bf;
    --photo-b: #c9a37f;
    --photo-c: #f3ead9;
    --rim: #ffffff;
  }
  * { box-sizing: border-box; margin: 0; padding: 0; }
  html, body { width: 1200px; height: 1000px; overflow: hidden; }
  body {
    background: linear-gradient(180deg, var(--board-top) 0%, var(--board-bottom) 100%);
    font-family: "PT Sans", Arial, sans-serif;
  }
  .board {
    position: absolute; left: 0; top: 0;
    width: 1036px; height: 863px;
    transform: scale(1.1583);
    transform-origin: 0 0;
  }
  .banner {
    position: absolute; overflow: hidden;
    background:
      radial-gradient(ellipse 120% 70% at 85% 110%, rgba(120,180,255,.35), transparent 60%),
      radial-gradient(ellipse 90% 60% at 10% 40%, rgba(10,30,90,.45), transparent 70%),
      linear-gradient(160deg, var(--blue-deep) 0%, var(--blue-mid) 55%, var(--blue-light) 100%);
    box-shadow: 0 1px 3px rgba(0,0,0,.2);
    color: var(--copy);
    font-weight: 700;
  }
  .photo {
    position: absolute;
    background:
      radial-gradient(circle at 30% 55%, var(--photo-b), transparent 45%),
      radial-gradient(circle at 70% 50%, var(--photo-a), transparent 50%),
      linear-gradient(135deg, var(--photo-c), var(--photo-a));
  }
  .photo--top {
    border-bottom: 4px solid var(--rim);
    border-radius: 0 0 50% 50% / 0 0 100% 100%;
  }
  .photo--side {
    border-right: 4px solid var(--rim);
    border-radius: 0 50% 50% 0 / 0 50% 50% 0;
  }
  .copy {
    position: absolute; text-align: center;
    display: flex; flex-direction: column; align-items: center;
  }
  .headline { color: var(--headline); line-height: 1.05; text-transform: uppercase; text-shadow: 0 1px 2px rgba(0,0,0,.35); }
  .headline em { font-style: italic; }
  .tagline { color: var(--copy); line-height: 1.2; text-shadow: 0 1px 2px rgba(0,0,0,.35); }
  .cta {
    position: absolute;
    display: flex; align-items: center; justify-content: center;
    border-radius: 999px;
    background: linear-gradient(180deg, var(--button-top) 0%, var(--button-bottom) 100%);
    border: 1px solid var(--button-edge);
    box-shadow: 0 2px 3px rgba(0,0,0,.35);
    color: var(--button-text);
    font-weight: 700;
  }

  /* 160x600 */
  .banner--skyscraper { left: 78px; top: 186px; width: 160px; height: 600px; }
  .banner--skyscraper .photo { left: -60px; top: -20px; width: 280px; height: 188px; }
  .banner--skyscraper .copy { left: 0; width: 160px; }
  .banner--skyscraper .headline-block { top: 203px; }
  .banner--skyscraper .l1 { font-size: 25px; }
  .banner--skyscraper .l2 { font-size: 25px; margin-top: 4px; }
  .banner--skyscraper .l3 { font-size: 16px; margin-top: 5px; }
  .banner--skyscraper .tagline-block { top: 333px; }
  .banner--skyscraper .t1 { font-size: 31px; }
  .banner--skyscraper .t2 { font-size: 21px; font-weight: 400; font-weight: 700; margin-top: 2px; }
  .banner--skyscraper .t3 { font-size: 21px; margin-top: 2px; }
  .banner--skyscraper .t4 { font-family: "PT Sans Narrow", "Arial Narrow", sans-serif; font-size: 44px; margin-top: 6px; }
  .banner--skyscraper .cta { left: 22px; top: 545px; width: 113px; height: 33px; font-size: 16px; }

  /* 216x36 */
  .banner--micro { left: 399px; top: 257px; width: 216px; height: 36px; }
  .banner--micro .photo { left: -10px; top: -14px; width: 60px; height: 64px; }
  .banner--micro .copy { left: 50px; width: 166px; top: 8px; }
  .banner--micro .headline { font-size: 8.5px; }
  .banner--micro .tagline { font-size: 8px; margin-top: 2px; }

  /* 300x50 */
  .banner--mobile { left: 634px; top: 243px; width: 300px; height: 50px; }
  .banner--mobile .photo { left: -14px; top: -18px; width: 90px; height: 86px; }
  .banner--mobile .copy { left: 76px; width: 224px; top: 12px; }
  .banner--mobile .headline { font-size: 11.5px; }
  .banner--mobile .tagline { font-size: 11px; margin-top: 3px; }

  /* 240x240 */
  .banner--square { left: 375px; top: 388px; width: 240px; height: 240px; }
  .banner--square .photo { left: -50px; top: -20px; width: 340px; height: 130px; }
  .banner--square .copy { left: 0; width: 240px; top: 115px; }
  .banner--square .headline { font-size: 16.5px; line-height: 1.3; font-weight: 400; }
  .banner--square .headline b { font-weight: 700; }
  .banner--square .tagline { font-size: 15.5px; margin-top: 6px; }
  .banner--square .cta { left: 78px; top: 210px; width: 84px; height: 24px; font-size: 12px; }

  /* 300x250 */
  .banner--rectangle { left: 644px; top: 383px; width: 300px; height: 250px; }
  .banner--rectangle .photo { left: -60px; top: -20px; width: 420px; height: 100px; }
  .banner--rectangle .copy { left: 0; width: 300px; top: 113px; }
  .banner--rectangle .headline { font-size: 24px; line-height: 1.2; }
  .banner--rectangle .tagline { font-size: 16px; margin-top: 4px; }
  .banner--rectangle .cta { left: 98px; top: 207px; width: 104px; height: 29px; font-size: 15px; }

  /* 728x90 */
  .banner--leaderboard { left: 251px; top: 696px; width: 728px; height: 90px; }
  .banner--leaderboard .photo { left: -30px; top: -30px; width: 196px; height: 150px; }
  .banner--leaderboard .copy { left: 166px; width: 420px; top: 18px; }
  .banner--leaderboard .headline { font-size: 24px; }
  .banner--leaderboard .tagline { font-size: 21.5px; margin-top: 7px; }
  .banner--leaderboard .cta { left: 605px; top: 36px; width: 113px; height: 33px; font-size: 16px; }
</style>
</head>
<body>
<main class="board">

  <section class="banner banner--skyscraper">
    <div class="photo photo--top" role="img" aria-label="Photo of a smiling family of three at home"></div>
    <div class="copy headline-block headline">
      <span class="l1">How safe</span>
      <span class="l2">is <em>your</em></span>
      <span class="l3">neighborhood?</span>
    </div>
    <div class="copy tagline-block tagline">
      <span class="t1">Protect</span>
      <span class="t2">Your Home</span>
      <span class="t3">and Family</span>
      <span class="t4">Today!</span>
    </div>
    <span class="cta">Lear more</span>
  </section>

  <section class="banner banner--micro">
    <div class="photo photo--side" role="img" aria-label="Photo of a smiling family of three"></div>
    <div class="copy">
      <span class="headline">How safe is <em>your</em> neighborhood?</span>
      <span class="tagline">Protect Your Home and Family Today!</span>
    </div>
  </section>

  <section class="banner banner--mobile">
    <div class="photo photo--side" role="img" aria-label="Photo of a smiling family of three"></div>
    <div class="copy">
      <span class="headline">How safe is <em>your</em> neighborhood?</span>
      <span class="tagline">Protect Your Home and Family Today!</span>
    </div>
  </section>

  <section class="banner banner--square">
    <div class="photo photo--top" role="img" aria-label="Photo of a smiling family of three at home"></div>
    <div class="copy">
      <span class="headline">How safe is<br><b><em>your</em></b> neighborhood?</span>
      <span class="tagline">Protect Your Home<br>and Family Today!</span>
    </div>
    <span class="cta">Lear more</span>
  </section>

  <section class="banner banner--rectangle">
    <div class="photo photo--top" role="img" aria-label="Photo of a smiling family of three at home"></div>
    <div class="copy">
      <span class="headline">How safe is<br><em>your</em> neighborhood?</span>
      <span class="tagline">Protect Your Home and Family Today!</span>
    </div>
    <span class="cta">Lear more</span>
  </section>

  <section class="banner banner--leaderboard">
    <div class="photo photo--side" role="img" aria-label="Photo of a smiling family of three at home"></div>
    <div class="copy">
      <span class="headline">How safe is <em>your</em> neighborhood?</span>
      <span class="tagline">Protect Your Home and Family Today!</span>
    </div>
    <span class="cta">Lear more</span>
  </section>

</main>
</body>
</html>
```